Modern Fun Bold Laundry stain remover wipes and spray

Marlo Basics packaging is bold, modern, and unapologetically real—just like the messes it’s made to handle.
please look at brand guidelines for colours and text etc. Please also just use sample text where descriptions etc need to go on packaging and i will fill in later.
3 die lines. 1 a box that will contain wipes - one the wipe packet and another is just sticker that will go on stain remover spray bottle

The design is clean but not precious. High contrast colors, strong typography, and plenty of breathing room give it a confident, fast-acting feel. The look says effective first, aesthetic second—but still looks damn good on a shelf or in a laundry room.

Typography is strong, modern, and slightly irreverent. Large, clear headlines deliver attitude up front, while short punchy lines replace traditional cleaning jargon. No scripts, no frills—just bold sans-serif type that feels sharp, capable, and honest.

Copy is conversational and fearless:

Speaks directly to the customer

Acknowledges real messes (stains, spills, toilets)

Never sugarcoats or over-explains

Confident without being aggressive

Funny without trying too hard

Visual elements are minimal but intentional—simple icons, soapy suds, bubbles, subtle texture, laundry tile feel or graphic blocks that hint at motion and speed. Nothing fussy. Nothing “clinical.” This is modern utility with personality.

The overall tone:

Fun but tough

Edgy but trustworthy

Modern without being cold

Relatable without being messy

Marlo doesn’t promise perfection—she promises results.

Shelf presence: bold, eye-catching, and instantly legible from a distance.
In-hand feel: sturdy, practical, and premium without being precious.
Brand energy: “I’ve got this.”

Get it dirty. Marlo will clean it.

logo, die lines and all ideas i like are uploaded

Target Market(s)

28-48 women

Industry/Entity Type

laundry cleaning

Font styles to use
Other font styles liked:
• all fonts and colours are in brand guidelines

Requirements
Must have
• Die line box - Front - Logo, Stain remover, Fast and effective, for clothes fabric and on the go messes, 25 wipes inside. Sides - ecofriendly, fast and effective, no harsh chemicals, Vegan, travel friendly, other side a fun tagline. Back. please just put sample text I will put proper text in
Should not have
• be boring an original

```html
<!DOCTYPE html>
<html lang="en">
<head>
<meta charset="utf-8">
<title>Marlo Basics — Packaging Dielines</title>
<link rel="stylesheet" href="https://fonts.googleapis.com/css2?family=DM+Mono:wght@400;500&family=Poppins:wght@400;500;700&display=swap">
<style>
  :root {
    --bg: #e0dafe;
    --panel: #a39dcb;
    --white: #ffffff;
    --label: #9a9a9a;
    --pattern-a: #cfcaea;
    --pattern-b: #b8b2dc;
    --art-top: #f1eef9;
    --art-bottom: #b6b0dc;
  }
  * { margin: 0; padding: 0; box-sizing: border-box; }
  html, body { width: 1200px; height: 1200px; overflow: hidden; background: var(--bg); }
  .sheet { display: block; width: 1200px; height: 1200px; }

  .section-label { font-family: "Poppins", sans-serif; font-weight: 400; font-size: 52px; fill: var(--label); }

  .panel { fill: var(--panel); stroke: var(--white); stroke-width: 16; stroke-linejoin: miter; }
  .panel-flat { fill: var(--panel); }
  .frame { fill: var(--white); }
  .rule { stroke: var(--white); stroke-width: 5; }
  .outline { fill: none; stroke: var(--white); stroke-width: 5; }
  .tag-box { fill: var(--panel); stroke: var(--white); stroke-width: 4; }
  .pattern-fill { fill: url(#patternTone); }
  .art-fill { fill: url(#artTone); }
  .step-box { fill: var(--white); }

  .wordmark { font-family: "Poppins", sans-serif; font-weight: 700; fill: var(--white); letter-spacing: -2px; }
  .mono { font-family: "DM Mono", monospace; font-weight: 500; fill: var(--white); }
  .body { font-family: "Poppins", sans-serif; font-weight: 400; fill: var(--white); }
</style>
</head>
<body>
<svg class="sheet" viewBox="0 0 1932 1932" xmlns="http://www.w3.org/2000/svg">
  <defs>
    <linearGradient id="patternTone" x1="0" y1="0" x2="1" y2="1">
      <stop offset="0" stop-color="var(--pattern-a)"/>
      <stop offset="1" stop-color="var(--pattern-b)"/>
    </linearGradient>
    <linearGradient id="artTone" x1="0" y1="0" x2="0" y2="1">
      <stop offset="0" stop-color="var(--art-top)"/>
      <stop offset="1" stop-color="var(--art-bottom)"/>
    </linearGradient>
  </defs>

  <!-- Sachet -->
  <g class="sachet">
    <text class="section-label" x="97" y="157">Sachet</text>
    <rect class="frame" x="98" y="187" width="920" height="345"/>
    <rect class="panel-flat" x="113" y="202" width="432" height="205"/>
    <text class="wordmark" x="329" y="333" font-size="125" text-anchor="middle">Marlo</text>
    <text class="mono" x="326" y="375" font-size="29" text-anchor="middle">STAIN REMOVER WIPES</text>
    <rect class="pattern-fill" x="113" y="410" width="432" height="108" role="img" aria-label="Wavy white and lilac swirl pattern"/>
    <rect class="tag-box" x="172" y="446" width="315" height="36" rx="18"/>
    <text class="body" x="329" y="471" font-size="20" text-anchor="middle">Fast &amp; effective on messes</text>
    <rect class="panel-flat" x="573" y="202" width="357" height="316"/>
    <rect class="pattern-fill" x="925" y="202" width="80" height="316" role="img" aria-label="Vertical strip of white wave pattern"/>
  </g>

  <!-- Spray label -->
  <g class="spray-label">
    <text class="section-label" x="1262" y="140">Spray label</text>
    <rect class="frame" x="1261" y="180" width="489" height="430"/>
    <rect class="panel-flat" x="1275" y="194" width="265" height="403"/>
    <text class="mono" font-size="26"><tspan x="1295" y="320">STAIN</tspan><tspan x="1295" y="346">REMOVER</tspan><tspan x="1295" y="372">SPRAY</tspan></text>
    <line class="rule" x1="1275" y1="384" x2="1407" y2="384"/>
    <text class="body" font-size="20"><tspan x="1296" y="415">for clothes</tspan><tspan x="1296" y="439">fabric</tspan></text>
    <rect class="outline" x="1275" y="460" width="127" height="45" rx="22" style="stroke-width:4"/>
    <text class="body" font-size="13" text-anchor="middle"><tspan x="1334" y="482">Fast &amp; effective</tspan><tspan x="1334" y="496">on messes</tspan></text>
    <text class="wordmark" transform="translate(1530 395) rotate(-90)" x="0" y="0" font-size="120" text-anchor="middle" textLength="380">Marlo</text>
    <rect class="pattern-fill" x="1553" y="194" width="184" height="403" role="img" aria-label="Bold white swirl pattern"/>
  </g>

  <!-- Box package -->
  <g class="box-dieline">
    <text class="section-label" x="135" y="1047">Box package</text>

    <!-- top flaps -->
    <rect class="panel" x="642" y="961" width="368" height="138"/>
    <rect class="panel" x="1010" y="644" width="518" height="81"/>
    <rect class="panel" x="1010" y="725" width="518" height="374"/>
    <rect class="panel" x="1528" y="961" width="365" height="138"/>

    <!-- main row -->
    <rect class="panel" x="42" y="1099" width="83" height="475"/>
    <rect class="panel" x="125" y="1099" width="517" height="475"/>
    <rect class="panel" x="642" y="1099" width="368" height="475"/>
    <rect class="panel" x="1010" y="1099" width="518" height="475"/>
    <rect class="panel" x="1528" y="1099" width="365" height="475"/>

    <!-- bottom flaps -->
    <polygon class="panel" points="125,1574 642,1574 642,1844 512,1844 512,1764 256,1764 256,1844 125,1844"/>
    <polygon class="panel" points="642,1574 1010,1574 1010,1844 846,1844 846,1706"/>
    <polygon class="panel" points="1010,1574 1528,1574 1394,1764 1394,1844 1150,1844 1150,1764"/>
    <polygon class="panel" points="1528,1574 1893,1574 1694,1706 1694,1844 1528,1844"/>

    <!-- lid (reads upside down on the flat) -->
    <g class="lid" transform="rotate(180 1269 910)">
      <text class="wordmark" x="1267" y="940" font-size="120" text-anchor="middle">Marlo</text>
      <text class="mono" x="1267" y="990" font-size="31" text-anchor="middle">STAIN REMOVER WIPES</text>
    </g>

    <!-- front -->
    <g class="front">
      <text class="wordmark" x="384" y="1250" font-size="160" text-anchor="middle">Marlo</text>
      <text class="mono" x="383" y="1296" font-size="33" text-anchor="middle">STAIN REMOVER WIPES</text>
      <rect class="frame" x="152" y="1330" width="462" height="195"/>
      <rect class="pattern-fill" x="157" y="1335" width="452" height="185" role="img" aria-label="White and lilac swirl pattern"/>
      <rect class="tag-box" x="246" y="1390" width="266" height="73"/>
      <text class="body" font-size="26" text-anchor="middle"><tspan x="379" y="1419">Fast &amp; effective</tspan><tspan x="379" y="1450">on real-life messes</tspan></text>
      <text class="mono" x="154" y="1556" font-size="24" style="font-weight:400">for clothes fabric</text>
      <text class="mono" x="612" y="1556" font-size="24" text-anchor="end" style="font-weight:400">25 wipes</text>
    </g>

    <!-- side: why -->
    <g class="side-why">
      <rect class="outline" x="690" y="1150" width="275" height="362" rx="20"/>
      <text class="mono" x="822" y="1194" font-size="30" text-anchor="middle">WHY MARLO?</text>
      <line class="rule" x1="690" y1="1212" x2="965" y2="1212"/>
      <g class="body" font-size="19">
        <circle cx="705" cy="1231" r="2.5" class="frame"/>
        <text><tspan x="717" y="1237">Cuts through everyday</tspan><tspan x="717" y="1259">stains, fast.</tspan></text>
        <circle cx="705" cy="1282" r="2.5" class="frame"/>
        <text><tspan x="717" y="1288">Safe for most fabrics.</tspan><tspan x="717" y="1313">Test on a hidden spot</tspan><tspan x="717" y="1335">first.</tspan></text>
        <circle cx="705" cy="1358" r="2.5" class="frame"/>
        <text><tspan x="717" y="1364">No harsh chemicals. No</tspan><tspan x="717" y="1386">fake “spring meadow”</tspan><tspan x="717" y="1408">lies.</tspan></text>
        <circle cx="705" cy="1432" r="2.5" class="frame"/>
        <text><tspan x="717" y="1438">Compact, ecofriendly,</tspan><tspan x="717" y="1462">and ready for on-the-go</tspan><tspan x="717" y="1484">disasters.</tspan></text>
      </g>
    </g>

    <!-- back -->
    <g class="back">
      <text class="mono" x="1269" y="1143" font-size="22" text-anchor="middle" style="font-weight:400">WHAT IT DOES</text>
      <text class="body" font-size="16.5" text-anchor="middle">
        <tspan x="1269" y="1170">[SAMPLE TEXT] These wipes are designed to lift fresh</tspan>
        <tspan x="1269" y="1189">stains and surface grime from everyday fabrics. Use</tspan>
        <tspan x="1269" y="1208">on clothing, soft furnishings and other washable</tspan>
        <tspan x="1269" y="1228">materials. Always check care labels.</tspan>
      </text>
      <line class="rule" x1="1018" y1="1253" x2="1520" y2="1253"/>
      <text class="mono" x="1269" y="1288" font-size="22" text-anchor="middle" style="font-weight:400">HOW TO USE</text>
      <rect class="step-box" x="1044" y="1302" width="136" height="98"/>
      <rect class="step-box" x="1201" y="1302" width="137" height="98"/>
      <rect class="step-box" x="1359" y="1302" width="137" height="98"/>
      <text class="body" font-size="16" text-anchor="middle"><tspan x="1112" y="1425">Step 1</tspan><tspan x="1266" y="1425">Step 2</tspan><tspan x="1415" y="1425">Step 3</tspan></text>
      <line class="rule" x1="1018" y1="1440" x2="1520" y2="1440"/>
      <text class="body" x="1269" y="1552" font-size="16" text-anchor="middle">Made for messy people, not perfect ones.</text>
    </g>

    <!-- side: tagline -->
    <g class="side-tagline">
      <rect class="art-fill" x="1548" y="1110" width="322" height="200" rx="30" role="img" aria-label="Playful soap-suds blob illustration"/>
      <rect class="tag-box" x="1578" y="1312" width="272" height="208" rx="22" style="stroke-width:5"/>
      <text class="mono" x="1594" y="1346" font-size="26" style="font-weight:400" textLength="232" lengthAdjust="spacingAndGlyphs">STAIN 1 - YOU 0</text>
      <line class="rule" x1="1578" y1="1362" x2="1850" y2="1362"/>
      <text class="mono" x="1594" y="1399" font-size="28" style="font-weight:400" textLength="232" lengthAdjust="spacingAndGlyphs">MARLO FIXES IT</text>
      <line class="rule" x1="1578" y1="1415" x2="1850" y2="1415"/>
      <text class="body" font-size="19"><tspan x="1594" y="1447">Throw it in your bag.</tspan><tspan x="1594" y="1472">Pretend you always have</tspan><tspan x="1594" y="1497">it together.</tspan></text>
    </g>
  </g>
</svg>
</body>
</html>
```